Health and wellnes company needs business cards

We are a Health and wellness business just relocated to Spain. Here nobody knows our business so we would like to put some of our services on the card. Clean design with logo.

Contact Information for Business Card

Brightmeadow
Karin & Tobias Edvall
Calle del Olivar 17
Villamar de la Costa
Mobile: 0046 731 402716
info@brightmeadow.example

Font styles to use
Serif

Colors
85cae6
85acd3
b768aa

Requirements
Must have
• these Services somewhere on the card
• - Private or group yoga
• - Reconnective healing
• - Kitesurfing lessons
• - Massage
• LOgo somewhere
Nice to have
• Colours that go with the logo please

```html
<!DOCTYPE html>
<html lang="en">
<head>
<meta charset="utf-8">
<title>Brightmeadow business card</title>
<link rel="stylesheet" href="https://fonts.googleapis.com/css2?family=Lato:wght@400;700;900&display=swap">
<style>
  :root {
    --navy: #1b3560;
    --teal: #5fb6b6;
    --ink: #1f1f1f;
    --paper: #ffffff;
    --paper-shade: #f1f1f1;
    --backdrop: #e6e3df;
  }
  * { margin: 0; padding: 0; box-sizing: border-box; }
  html, body { width: 1200px; height: 900px; overflow: hidden; }
  body {
    background: var(--backdrop);
    font-family: "Lato", sans-serif;
    color: var(--ink);
    position: relative;
  }
  .card {
    position: absolute;
    left: 270px;
    width: 660px;
    height: 377px;
    background: linear-gradient(160deg, var(--paper) 0%, var(--paper-shade) 100%);
    border-bottom: 5px solid var(--navy);
    box-shadow: 0 6px 18px rgba(0,0,0,0.12);
  }
  .card--front { top: 48px; }
  .card--back { top: 475px; }

  /* brand lockup */
  .brand {
    position: absolute;
    display: flex;
    flex-direction: column;
    align-items: center;
    gap: 14px;
  }
  .brand__dot {
    border-radius: 50%;
    background: var(--teal);
  }
  .brand__name {
    font-family: "Lato", sans-serif;
    font-weight: 700;
    color: var(--navy);
    text-transform: uppercase;
    letter-spacing: 0.04em;
    white-space: nowrap;
  }
  .card--front .brand { left: 40px; top: 62px; width: 260px; }
  .card--front .brand__dot { width: 84px; height: 84px; }
  .card--front .brand__name { font-size: 27px; }
  .card--back .brand { left: 0; right: 0; top: 78px; }
  .card--back .brand__dot { width: 112px; height: 112px; }
  .card--back .brand__name { font-size: 46px; }

  /* contact block */
  .contact {
    position: absolute;
    left: 340px;
    top: 52px;
  }
  .contact__names {
    font-weight: 900;
    font-size: 25px;
    color: var(--teal);
    margin-bottom: 8px;
    white-space: nowrap;
  }
  .contact__names .first { color: var(--navy); }
  .contact__line {
    font-size: 15px;
    line-height: 21px;
  }
  .contact__item {
    display: flex;
    align-items: center;
    gap: 12px;
    font-size: 15px;
    line-height: 24px;
  }
  .contact__item:first-of-type { margin-top: 4px; }
  .contact__icon { width: 20px; height: 16px; fill: var(--navy); flex: none; }

  /* services */
  .services {
    position: absolute;
    left: 0;
    right: 0;
    top: 248px;
    display: flex;
    justify-content: center;
    align-items: stretch;
    gap: 26px;
  }
  .services__col {
    display: flex;
    flex-direction: column;
    gap: 14px;
    justify-content: center;
  }
  .services__col--left { align-items: flex-end; }
  .services__divider { width: 1.5px; background: var(--navy); }
  .service {
    display: flex;
    align-items: center;
    gap: 14px;
    font-size: 17px;
  }
  .service__icon {
    width: 24px;
    height: 24px;
    border-radius: 50%;
    background: var(--navy);
    flex: none;
  }
</style>
</head>
<body>
  <section class="card card--front" aria-label="Business card front">
    <div class="brand">
      <span class="brand__dot" aria-hidden="true"></span>
      <span class="brand__name">Brightmeadow</span>
    </div>

    <div class="contact">
      <p class="contact__names"><span class="first">Karin</span> &amp; Tobias Edvall</p>
      <p class="contact__line">Calle del Olivar 17</p>
      <p class="contact__line">Villamar de la Costa</p>
      <p class="contact__item">
        <svg class="contact__icon" viewBox="0 0 20 16" aria-hidden="true">
          <path d="M1 5c0-2 4-4 9-4s9 2 9 4v1.5h-4.5V5h-9v1.5H1z"/>
          <path d="M4 8h12l1.5 7h-15z"/>
          <circle cx="10" cy="11" r="2" fill="#fff"/>
        </svg>
        0046 731 402716
      </p>
      <p class="contact__item">
        <svg class="contact__icon" viewBox="0 0 20 16" aria-hidden="true">
          <path d="M1 2h18v12H1z"/>
          <path d="M1.5 2.5l8.5 6.5 8.5-6.5M1.5 13.5l6-5.5M18.5 13.5l-6-5.5" stroke="#fff" stroke-width="1.3" fill="none"/>
        </svg>
        info@brightmeadow.example
      </p>
    </div>

    <div class="services">
      <div class="services__col services__col--left">
        <p class="service">Private or group yoga <span class="service__icon" role="img" aria-label="Yoga pose icon"></span></p>
        <p class="service">Reconnective healing <span class="service__icon" role="img" aria-label="Healing heart-sun icon"></span></p>
      </div>
      <span class="services__divider" aria-hidden="true"></span>
      <div class="services__col">
        <p class="service"><span class="service__icon" role="img" aria-label="Kitesurfer icon"></span> Kitesurfing lessons</p>
        <p class="service"><span class="service__icon" role="img" aria-label="Massage icon"></span> Massage</p>
      </div>
    </div>
  </section>

  <section class="card card--back" aria-label="Business card back">
    <div class="brand">
      <span class="brand__dot" aria-hidden="true"></span>
      <span class="brand__name">Brightmeadow</span>
    </div>
  </section>
</body>
</html>
```